brochure for high-end senior living company

We need a new brochure that we can pass out to doctors and social workers so they would choose us over the competition.
brightmeadowhaven.example is our website that shows our colors and themes

we stand out over our competition due to our high quality of staff and our staff to resident ratio.
We are not afraid of difficult and complex care situations. Instead, we thrive on coordinating complexity.

We do all of this in a lovely setting that is luxurious and feels like home.

Target Market(s)

The families who make the decision are 60-70 years old. They are not not "rich" but they have saved well and usually have more than 1 million in assets.

Industry/Entity Type

Senior Living, Memory Care

Font styles to use
Serif

Colors
00AB8E
00BBA5
67D7C9
C6EFE9
E9F9F6
FFC000
F8CF3A
FAE287
FDF2CF
FEFAEE

Requirements
Must have
• When compromise is not an option...
Nice to have
• A difficult balance of beautiful and activities (happy people), but also communicating that we handle difficult and complex care.

```html
<!DOCTYPE html>
<html lang="en">
<head>
<meta charset="utf-8">
<title>Bright Meadow Haven – Tri-fold Brochure</title>
<link rel="stylesheet" href="https://fonts.googleapis.com/css2?family=Aleo:wght@400;500;600&family=Raleway:wght@400;500;600&display=swap">
<style>
:root{
  --green:#1f5b45;
  --green-deep:#174a38;
  --gold:#c9a227;
  --gold-soft:#d9b440;
  --paper:#ffffff;
  --ink:#2b2b2b;
  --stage:#8d8d8d;
  --photo-warm:#b98b6a;
}
*{box-sizing:border-box;margin:0;padding:0}
html,body{width:1200px;height:2400px;overflow:hidden}
body{background:var(--stage);font-family:"Raleway",sans-serif;color:var(--ink);position:relative}
.sheet{position:absolute;left:40px;width:1120px;height:790px;background:var(--paper);display:flex;box-shadow:0 10px 30px rgba(0,0,0,.25)}
.sheet--outside{top:270px}
.sheet--inside{top:1340px}
.panel{width:373.33px;height:100%;position:relative;padding:26px 30px}
h2{font-family:"Aleo",serif;font-weight:500;color:var(--green);font-size:23px;line-height:1.05}
h3{font-family:"Aleo",serif;font-weight:500;color:var(--green);font-size:18px;line-height:1.1}
.rule{display:block;height:3px;background:var(--gold);margin:4px 0 10px}
.lead{color:var(--gold);font-size:13px;line-height:1.25;margin-bottom:10px}
p{font-size:12.4px;line-height:1.32;text-align:justify;margin-bottom:10px}
.photo{display:block;border-radius:0}

/* cover */
.cover{padding:0}
.brand{padding:34px 30px 0;text-align:center}
.brand__name{font-family:"Aleo",serif;font-weight:500;color:var(--ink);font-size:42px;letter-spacing:1px;line-height:1}
.brand__tag{font-family:"Aleo",serif;font-size:22px;color:var(--ink);margin-top:6px;border-top:2px solid var(--gold);padding-top:4px;display:inline-block}
.cover__headline{font-family:"Aleo",serif;font-weight:500;color:var(--green);font-size:31px;line-height:1.1;padding:36px 25px 0}
.cover__rule{width:290px;height:4px;background:var(--gold);margin:6px 0 0 25px}
.cover__photo{position:absolute;left:0;top:262px;width:100%;height:440px;background:linear-gradient(160deg,#e4ddd6 0%,#c9b4a3 40%,#a7322f 75%,#7a2a2a 100%)}
.call{position:absolute;left:0;bottom:0;width:100%;height:90px;background:var(--green);padding-left:36px;text-align:center;color:#fff}
.call::before{content:"";position:absolute;left:0;top:0;width:36px;height:100%;background:var(--gold)}
.call__label{font-family:"Aleo",serif;color:var(--gold-soft);font-size:22px;padding-top:12px}
.call__phone{font-family:"Aleo",serif;font-size:26px;margin-top:4px}

.care-photo{width:312px;height:345px;margin:12px 0 14px;border:6px solid var(--gold);background:linear-gradient(170deg,#f1e3b6 0%,#d9c18a 45%,#8b6a4c 100%)}

/* reasons */
.reasons{background:var(--green);padding:8px;margin-top:-4px}
.reasons__inner{border:2px dashed var(--gold);padding:14px 16px 12px;color:#fff}
.reasons__title{font-family:"Aleo",serif;font-size:21px;text-align:center;margin-bottom:16px}
.reason{display:flex;align-items:center;gap:14px;font-weight:600;font-size:12.6px;line-height:1.2;min-height:34px}
.reason svg{flex:0 0 26px}
.loc-heading{font-family:"Aleo",serif;font-weight:500;font-size:21px;color:var(--green);margin:14px 0 6px;display:inline-block;border-bottom:2px solid var(--gold)}
.locations{background:var(--green);padding:6px;display:flex;flex-direction:column;gap:6px}
.loc{height:143px;position:relative;padding:0 8px 4px;display:flex;flex-direction:column;justify-content:flex-end;color:#fff;font-size:15px;line-height:1.25}
.loc--1{background:linear-gradient(180deg,#9fb78e 0%,#6f8560 50%,#4b4a4a 100%)}
.loc--2{background:linear-gradient(120deg,#7b8f8c 0%,#a98a82 50%,#54405a 100%)}
.loc--3{background:linear-gradient(120deg,#a59a8a 0%,#8a6f94 50%,#4d4a3e 100%)}
.loc__name{color:var(--gold-soft);font-weight:600}

/* inside */
.inside-left::before{content:"";position:absolute;left:0;top:0;width:9px;height:470px;background:var(--gold)}
.inside-right::after{content:"";position:absolute;right:0;top:318px;width:9px;height:472px;background:var(--gold)}
.rule--short{width:118px}
.inside-photo-a{width:314px;height:175px;margin:6px 0 18px;background:linear-gradient(110deg,#2e2418 0%,#8a6a42 45%,#d9b073 70%,#5b4733 100%)}
.inside-photo-b{width:314px;height:205px;margin:4px 0 16px;background:linear-gradient(150deg,#d9d4cc 0%,#b9a79a 45%,#6d6a7a 100%)}
.inside p{font-size:12.2px;line-height:1.28;margin-bottom:8px}
.inside .lead{font-size:13px;margin-bottom:6px}
.inside h3{margin-bottom:2px}
.badge{position:absolute;left:30px;bottom:20px;width:300px;height:84px;border:2px solid var(--green);border-radius:42px;text-align:center;padding-top:12px}
.badge__name{font-family:"Aleo",serif;font-weight:500;font-size:28px;color:var(--ink);line-height:1}
.badge__tag{font-family:"Aleo",serif;font-size:15px;color:var(--ink);margin-top:6px}
</style>
</head>
<body>

<section class="sheet sheet--outside" aria-label="Brochure outside">
  <div class="panel cover">
    <div class="brand">
      <div class="brand__name">Bright Meadow</div>
      <div class="brand__tag">Residential Assisted Living</div>
    </div>
    <h1 class="cover__headline">When compromise is not an option...</h1>
    <div class="cover__rule"></div>
    <div class="cover__photo photo" role="img" aria-label="Smiling senior resident in a red cardigan holding oversized playing cards"></div>
    <div class="call">
      <div class="call__label">Give Us a Call Today</div>
      <div class="call__phone">(555) 014-2290</div>
    </div>
  </div>

  <div class="panel">
    <h2>Your Loved Ones Are in Good Hands</h2>
    <span class="rule" style="width:200px"></span>
    <div class="lead">we stand out over our competition due to our high quality of staff and our staff to resident ratio</div>
    <p>First and foremost, our Westfield staff members are genuinely passionate about caring for others. Regardless of age, we believe that every individual is an equal who deserves to be treated with respect and dignity, and we hope that our community is an accurate reflection of that.</p>
    <div class="care-photo photo" role="img" aria-label="Caregiver dancing with an elderly resident in a yellow shirt"></div>
    <p>To provide the highest level of care possible for our residents, we keep a high staff ratio - the highest ratio of staff-to-residents that the assisted living industry has to offer. In doing so, we form close relationships with our residents, which allows us to not only get to know each resident personally, but also allows us to quickly and accurately assess changes in level of care.</p>
  </div>

  <div class="panel">
    <div class="reasons">
      <div class="reasons__inner">
        <div class="reasons__title">Reasons to Choose Us</div>
        <div class="reason">
          <svg width="26" height="26" viewBox="0 0 26 26" aria-hidden="true"><rect width="26" height="26" fill="#c9a227"/><path d="M5 18V8M5 14h16v4M9 14v-3h10a2 2 0 0 1 2 2v1" stroke="#fff" stroke-width="1.8" fill="none"/></svg>
          <span>Private Rooms and Bathrooms</span>
        </div>
        <div class="reason">
          <svg width="26" height="26" viewBox="0 0 26 26" aria-hidden="true"><rect width="26" height="26" fill="#c9a227"/><circle cx="13" cy="13" r="6.5" stroke="#fff" stroke-width="1.8" fill="none"/><path d="M4 6v14M22 6v14" stroke="#fff" stroke-width="1.8"/></svg>
          <span>Delicious and Healthy Home Cooked Meals</span>
        </div>
        <div class="reason">
          <svg width="26" height="26" viewBox="0 0 26 26" aria-hidden="true"><rect width="26" height="26" fill="#c9a227"/><path d="M13 15s-5-3-5-6a2.5 2.5 0 0 1 5-1 2.5 2.5 0 0 1 5 1c0 3-5 6-5 6zM4 19h11l6-3" stroke="#fff" stroke-width="1.6" fill="none"/></svg>
          <span>Highest Caregiver to Resident Ratio in the Industry</span>
        </div>
        <div class="reason">
          <svg width="26" height="26" viewBox="0 0 26 26" aria-hidden="true"><rect width="26" height="26" fill="#c9a227"/><circle cx="13" cy="13" r="8" stroke="#fff" stroke-width="1.8" fill="none"/><path d="M13 8v5l3 2" stroke="#fff" stroke-width="1.8" fill="none"/></svg>
          <span>24/7 Well-Trained Caregivers on Site</span>
        </div>
      </div>
    </div>
    <div class="loc-heading">LOCATION</div>
    <div class="locations">
      <div class="loc loc--1 photo" role="img" aria-label="Residents dining together on an outdoor patio">
        <span class="loc__name">Bright Meadow Westfield</span>
        <span>1200 Orchard Ave</span>
        <span>1200 Orchard Ave, Westfield, CA 90001</span>
      </div>
      <div class="loc loc--2 photo" role="img" aria-label="Caregiver smiling beside a senior man">
        <span class="loc__name">Bright Meadow Linden</span>
        <span>450 Linden Way</span>
        <span>450 Linden Way, Cedar Oaks, CA 90002</span>
      </div>
      <div class="loc loc--3 photo" role="img" aria-label="Senior resident and caregiver sharing a moment indoors">
        <span class="loc__name">Bright Meadow Quail Hollow</span>
        <span>77 Quail Hollow Ln</span>
        <span>77 Quail Hollow Ln, Westfield, CA 90001</span>
      </div>
    </div>
  </div>
</section>

<section class="sheet sheet--inside inside" aria-label="Brochure inside">
  <div class="panel inside-left">
    <h2>We're Not Afraid of a Challenge</h2>
    <span class="rule rule--short"></span>
    <div class="lead">We are not afraid of difficult and complex care situations. Instead, we thrive on coordinating complexity.</div>
    <div class="inside-photo-a photo" role="img" aria-label="Caregiver playing a floor game with a resident in a warm living room"></div>
    <h3>Assisted Living for Alzheimer's &amp; Dementia</h3>
    <div class="lead">The Safety &amp; Warmth of a Real Home In Westfield</div>
    <p>For those with loved ones who are suffering from either Alzheimer's disease or dementia, come and visit our Stone Harbor assisted living home to learn more about our family-focused care home. All Bright Meadow Haven Residential Assisted Living employs a team of experienced caregivers and licensed medical professionals who understand how these diseases work, and how to provide effective treatment to help residents cope with such conditions. This is not a resort or a sterile nursing community. We are a home environment run by professionals who care about helping people. We are passionate about providing our residents with the highest quality of life possible in a pleasant atmosphere, surrounded by people who genuinely care for their needs.</p>
  </div>

  <div class="panel">
    <h3>Hospice Care in Westfield</h3>
    <div class="lead">We'll Treat Your Loved One Like Family:</div>
    <p>All Bright Meadow Haven Residential Assisted Living is known for providing superior assisted living care that is compassionate, attentive, and caring. Our Westfield assisted living home has become recognized for providing world class care and treatment to the elderly and to those who need additional daily assistance. We employ a team that is trained, experienced, and share a passion for dedicated care. From beautiful communities and delicious meals to 24-hour assistance, we work hard to create a relaxing and stress-free environmenta</p>
    <div class="inside-photo-b photo" role="img" aria-label="Smiling resident making a beaded craft at a table"></div>
    <h3>Stroke Patient Assisted Living in Westfield &amp; Riverton</h3>
    <div class="lead">We'll Treat Your Loved One Like Family</div>
    <p>At our Westfield assisted living home, we understand the enormous change that can occur after a loved one has suffered a stroke. As such, we take the time to understand each resident's unique situation in order to accommodate their needs. Our goal is to provide a safe environment that is both secure and comfortable for all of our valued residents.</p>
    <p>Strokes can result in brain damage that impairs verbal and mental capabilities. Our home environment and professional care, combined with our highly trained and dedicated team, ensures patients receive treatment and compassionate care at all</p>
  </div>

  <div class="panel inside-right">
    <h3>Parkinson's Care in Westfield</h3>
    <div class="lead">We'll Treat Your Loved One Like Family</div>
    <p>If your loved one suffers from Parkinson's disease, All Bright Meadow Haven Residential Assisted Living can provide the assistance and compassionate care you need to feel comfortable and at home. Due to damage in the central nervous system, residents who have been diagnosed with Parkinson's disease often experience tremors, muscle rigidity, and changes in speech. Our highly trained and experienced team of Westfield assisted living professionals has the medical training and compassion to help make life for our senior residents as pleasant and comfortable as possible.</p>
    <h3>Limited Mobility Assisted Living</h3>
    <div class="lead">Put Your Trust in Bright Meadow Haven Residential Assisted Living in Westfield &amp; Riverton</div>
    <p>Are you looking for an inviting and beautiful assisted living home in Westfield for your elderly loved one? Look no further than Bright Meadow Haven Residential Assisted Living. For many years, we have served the families from Westfield and Riverton area by providing the most dedicated assisted living services to the elderly and to those who need more assistance in their daily life. If your loved one is struggling with his or her mobility, place your trust in our committed team to supply superior care.</p>
    <p>Our emphasis on quality care from a compassionate team of caregivers has given us the reputation as one of the leading care facilities in our community. We look to continue our tradition of excellence by serving you today. We have beautiful facilities, healthy meals, and a dedicated staff that works hard to provide our residents with care and attention 24/7. Don't hesitate to call us at (555) 014-2291 with any questions that you may have!</p>
    <div class="badge">
      <div class="badge__name">Bright Meadow</div>
      <div class="badge__tag">Residential Assisted Living</div>
    </div>
  </div>
</section>

</body>
</html>
```